New Trade Show Booth Design Project

We are a security system integrator. Please visit www.kelmoridge.com for info. we would like a simple design that might or might not includes our logo (attached) and a background image. Not sure what that image will be, but it has to project what we do. Maybe a single surveillance camera (attached). The tag line should be " KRP Technology - Security Systems Integration"

Target Market(s)

Municipalities, schools, police departments

Font styles to use
Serif
Sans Serif

Requirements
Nice to have
• Bullet points:
Design
Installation
Service
Support

```html
<!DOCTYPE html>
<html lang="en">
<head>
<meta charset="utf-8">
<title>KRP Technology - Security Systems Integration</title>
<link rel="stylesheet" href="https://fonts.googleapis.com/css2?family=Syncopate:wght@700&family=Russo+One&family=Oswald:wght@600&family=Montserrat:wght@800&display=swap">
<style>
  :root {
    --backdrop: #e9eaec;
    --navy-deep: #061338;
    --band-blue: #1b3764;
    --brand-red: #c21f26;
    --white: #ffffff;
    --photo-dark: #161b2c;
    --photo-light: #dfe2ea;
  }
  html, body {
    margin: 0;
    padding: 0;
    width: 1200px;
    height: 973px;
    overflow: hidden;
    background: var(--backdrop);
  }
  .booth-panel {
    position: absolute;
    left: 0;
    top: 51px;
    width: 1200px;
    height: 871px;
    display: block;
  }
  .headline { font-family: "Syncopate", "Arial Black", sans-serif; font-weight: 700; fill: var(--white); }
  .service-label { font-family: "Russo One", "Arial Black", sans-serif; fill: var(--white); font-size: 27px; }
  .cta-text { font-family: "Oswald", "Arial Narrow", sans-serif; font-weight: 600; font-size: 50px; }
  .web-address { font-family: "Montserrat", Arial, sans-serif; font-weight: 800; font-size: 34px; fill: var(--white); letter-spacing: 11px; }
  .icon-ring { fill: var(--white); stroke: var(--brand-red); stroke-width: 4; }
  .icon-line { fill: none; stroke: var(--brand-red); stroke-width: 3; stroke-linecap: round; stroke-linejoin: round; }
</style>
</head>
<body>
<svg class="booth-panel" viewBox="0 0 1200 871" xmlns="http://www.w3.org/2000/svg">
  <defs>
    <linearGradient id="skyGradient" x1="0" y1="0" x2="1" y2="1">
      <stop offset="0" stop-color="#1f3f8f"/>
      <stop offset="0.5" stop-color="var(--navy-deep)"/>
      <stop offset="1" stop-color="#1d44a0"/>
    </linearGradient>
    <linearGradient id="photoGradient" x1="0" y1="0" x2="1" y2="0">
      <stop offset="0" stop-color="var(--photo-dark)"/>
      <stop offset="0.5" stop-color="#2c3248"/>
      <stop offset="0.8" stop-color="#b7bdcf"/>
      <stop offset="1" stop-color="var(--photo-light)"/>
    </linearGradient>
    <radialGradient id="cameraGradient" cx="0.45" cy="0.45" r="0.7">
      <stop offset="0" stop-color="#f4f5f8"/>
      <stop offset="0.6" stop-color="#c9cedb"/>
      <stop offset="1" stop-color="#7d869e"/>
    </radialGradient>
  </defs>

  <!-- header backdrop -->
  <rect class="header-backdrop" x="0" y="0" width="1200" height="206" fill="url(#skyGradient)" role="img" aria-label="Blue digital network background"/>

  <!-- scene photo area -->
  <rect class="scene-photo" x="0" y="206" width="1200" height="506" fill="url(#photoGradient)" role="img" aria-label="Dim hallway background behind the camera"/>

  <!-- camera photo placeholder -->
  <rect class="camera-photo" x="640" y="332" width="560" height="330" rx="150" fill="url(#cameraGradient)" role="img" aria-label="Photo of a white dome surveillance camera on a wall mount"/>

  <!-- brand title -->
  <text class="headline brand-name" x="600" y="139" text-anchor="middle" font-size="52" textLength="689" lengthAdjust="spacingAndGlyphs">KRP TECHNOLOGY</text>

  <!-- red divider line -->
  <rect x="0" y="199" width="1200" height="5" fill="var(--brand-red)"/>

  <!-- security systems band -->
  <polygon class="band-red" points="149,165 1072,165 1048,246 127,246" fill="var(--brand-red)"/>
  <text class="headline" x="600" y="225" text-anchor="middle" font-size="56" textLength="805" lengthAdjust="spacingAndGlyphs">SECURITY SYSTEMS</text>

  <!-- integration band -->
  <polygon class="band-blue" points="241,246 939,246 959,322 270,322" fill="var(--band-blue)"/>
  <rect x="270" y="322" width="689" height="3" fill="var(--white)"/>
  <text class="headline" x="600" y="302" text-anchor="middle" font-size="56" textLength="533" lengthAdjust="spacingAndGlyphs">INTEGRATION</text>

  <!-- services -->
  <g class="service-item design">
    <circle class="icon-ring" cx="262" cy="399" r="45"/>
    <g class="icon-line">
      <path d="M240 381 L276 417 L284 419 L282 411 L246 375 Z"/>
      <path d="M280 377 L244 413 L240 421 L248 419 L284 383 Z"/>
    </g>
    <polygon points="183,454 352,454 340,493 171,493" fill="var(--brand-red)"/>
    <text class="service-label" x="262" y="484" text-anchor="middle">Design</text>
  </g>
  <g class="service-item installation">
    <circle class="icon-ring" cx="474" cy="399" r="45"/>
    <g class="icon-line">
      <rect x="455" y="378" width="22" height="40"/>
      <path d="M460 386 H472 M460 394 H472 M460 410 V414 M465 410 V414"/>
      <circle cx="488" cy="407" r="8"/>
      <circle cx="488" cy="407" r="3"/>
    </g>
    <polygon points="364,454 594,454 582,493 352,493" fill="var(--brand-red)"/>
    <text class="service-label" x="474" y="484" text-anchor="middle">Installation</text>
  </g>
  <g class="service-item service">
    <circle class="icon-ring" cx="262" cy="557" r="45"/>
    <g class="icon-line">
      <path d="M244 539 L280 575 M280 539 L244 575"/>
      <circle cx="284" cy="535" r="6"/>
      <circle cx="241" cy="578" r="5"/>
    </g>
    <polygon points="183,616 352,616 340,655 171,655" fill="var(--brand-red)"/>
    <text class="service-label" x="262" y="646" text-anchor="middle">Service</text>
  </g>
  <g class="service-item support">
    <circle class="icon-ring" cx="474" cy="557" r="45"/>
    <g class="icon-line">
      <path d="M456 560 A18 18 0 0 1 492 560"/>
      <rect x="451" y="556" width="8" height="16" rx="3"/>
      <rect x="489" y="556" width="8" height="16" rx="3"/>
      <path d="M493 572 L493 580 L480 584"/>
      <circle cx="477" cy="584" r="3"/>
    </g>
    <polygon points="364,616 594,616 582,655 352,655" fill="var(--brand-red)"/>
    <text class="service-label" x="474" y="646" text-anchor="middle">Support</text>
  </g>

  <!-- bottom band -->
  <rect x="0" y="712" width="1200" height="159" fill="var(--brand-red)"/>
  <rect x="0" y="708" width="1200" height="4" fill="var(--white)"/>

  <!-- call to action -->
  <rect class="cta-pill" x="185" y="679" width="470" height="62" rx="31" fill="var(--band-blue)"/>
  <rect class="phone-pill" x="620" y="679" width="392" height="62" rx="31" fill="var(--white)"/>
  <text class="cta-text" x="224" y="731" fill="var(--white)" textLength="370" lengthAdjust="spacingAndGlyphs">FREE CONSULTATION</text>
  <circle cx="648" cy="706" r="40" fill="var(--white)" stroke="var(--brand-red)" stroke-width="5"/>
  <path class="phone-icon" d="M636 688 L645 686 L650 698 L644 702 Q648 713 657 719 L662 713 L673 719 L671 728 Q664 733 655 729 Q639 718 633 700 Q632 692 636 688 Z" fill="var(--brand-red)"/>
  <text class="cta-text" x="701" y="731" fill="var(--brand-red)" textLength="274" lengthAdjust="spacingAndGlyphs">1.800.555.0142</text>

  <text class="web-address" x="600" y="800" text-anchor="middle">www.kelmoridge.com</text>
</svg>
</body>
</html>
```